Flyer for a company who uses pure argan oil

so we need a folder of 4 pages. including front & back.
unfolded format:
10cm wide by 6.5cm high.

Front card - as background use picture file 'front'
in the lower feathers in these languages ​​'thank you'
Thank you Bedankt Merci Danke
Shukran Grazie Tak Kop khun
Arigatô Hvala Dankie Mahalo
Please use a suitable font as on the bottle.

Back of card - as background use picture file 'back'
again in the lower springs
'Yes Kavro is here'

Inside of the folding card fitting and soft pink background.

With the following text:
Wist u dat het Kavro team alles zelf doet, van de noot tot in het flesje.
Met Kavro koopt u een 100% puur natuurproduct: volledig vrij van toevoegingen en bewaarmiddelen.
U geeft uw huid, haar, nagels de allerbeste verzorging, op elk moment van de dag!
Psoriasis, droge huid, eczeem, anti aging en zoveel meer voor heel het gezin.

''Translations of the text in English so you can understand it''
Did you know that the Kavro team does everything itself, from the nut to the bottle. With Kavro you buy a 100% pure natural product: completely free of additives and preservatives. You give your skin, hair and nails the very best care, at any time of the day! Psoriasis, dry skin, eczema, anti-aging and so much more for the whole family.

A new text with the title 'PURE HEILZAAMHEID IN ÉÉN TOPPRODUCT '
And then these 3 benefits under the title.
● Een allesomvattende dag- en nachtverzorging

● Hydraterende en egaliserende eigenschappen

● Herstellend bij huid-, haar- en nagel kwaaltjes

And then somewhere else maybe in a banner or green circle
Vegan - niet getest op dieren - 100% ongeraffineerde Argan olie

Vegan - not tested on animals - 100% unrefined Argan oil

Thanks!!

```html
<!DOCTYPE html>
<html lang="nl">
<head>
<meta charset="utf-8">
<title>Kavro argan oil – folding card</title>
<link rel="stylesheet" href="https://fonts.googleapis.com/css2?family=Open+Sans:ital,wght@0,400;0,600;0,700;0,800;1,400;1,600&family=Pacifico&family=Sorts+Mill+Goudy&display=swap">
<style>
  :root {
    --stage: #5a5a5a;
    --paper: #ffffff;
    --coral: #f26b78;
    --coral-deep: #ec5566;
    --blush: #f8d4d3;
    --feather: #f5cfc2;
    --feather-soft: #fbe8e1;
    --amber: #b5631f;
    --amber-dark: #7a3a10;
    --title-red: #e3303c;
    --ink: #2b2b2b;
    --ink-soft: #555555;
    --frame: #6f6f6f;
    --vegan: #66c12b;
    --vegan-dark: #3f8f17;
  }
  * { box-sizing: border-box; margin: 0; padding: 0; }
  html, body { width: 900px; height: 1200px; overflow: hidden; }
  body {
    background: var(--stage);
    font-family: "Open Sans", Arial, sans-serif;
    color: var(--ink);
    position: relative;
  }
  .spread {
    position: absolute;
    left: 40px;
    width: 820px;
    height: 533px;
    background: var(--paper);
    overflow: hidden;
    box-shadow: 0 6px 18px rgba(0,0,0,.35);
  }
  .spread--outside { top: 40px; }
  .spread--inside { top: 627px; }
  .spread::after {
    content: "";
    position: absolute;
    left: 395px; top: 0;
    width: 30px; height: 100%;
    background: linear-gradient(90deg, rgba(0,0,0,0), rgba(0,0,0,.07) 50%, rgba(0,0,0,0));
    pointer-events: none;
  }
  .abs { position: absolute; }

  /* feather photo placeholders */
  .feathers { position: absolute; }
  .feathers--back {
    left: 0; top: 0; width: 410px; height: 533px;
    background:
      radial-gradient(ellipse 60% 30% at 50% 75%, var(--feather) 0%, rgba(245,207,194,0) 70%),
      radial-gradient(ellipse 50% 25% at 20% 18%, var(--feather-soft) 0%, rgba(251,232,225,0) 70%);
  }
  .feathers--front {
    left: 410px; top: 0; width: 410px; height: 533px;
    background:
      radial-gradient(ellipse 70% 25% at 50% 72%, var(--feather) 0%, rgba(245,207,194,0) 70%),
      radial-gradient(ellipse 35% 25% at 95% 30%, var(--feather-soft) 0%, rgba(251,232,225,0) 70%),
      radial-gradient(ellipse 40% 20% at 10% 10%, var(--feather-soft) 0%, rgba(251,232,225,0) 70%);
  }
  .feathers--inside {
    left: 0; top: 0; width: 820px; height: 533px;
    background:
      linear-gradient(180deg, var(--feather) 0%, rgba(245,207,194,.55) 14%, rgba(255,255,255,0) 34%),
      radial-gradient(ellipse 20% 40% at 100% 40%, var(--feather-soft) 0%, rgba(251,232,225,0) 70%),
      radial-gradient(ellipse 28% 40% at 0% 60%, var(--feather-soft) 0%, rgba(251,232,225,0) 70%);
  }

  /* bottle photo placeholders */
  .bottle {
    position: absolute;
    border-radius: 14px 14px 10px 10px;
    background: linear-gradient(180deg, #eeeeee 0%, #eeeeee 20%, var(--amber) 24%, var(--amber-dark) 100%);
  }
  .bottle--dropper { left: 158px; top: 93px; width: 99px; height: 273px; }
  .bottle--spray { left: 554px; top: 87px; width: 106px; height: 279px; }

  /* back panel contact */
  .back-accent { left: 0; top: 403px; width: 16px; height: 109px; background: var(--coral); }
  .contact { left: 68px; top: 412px; width: 300px; }
  .contact__row { display: flex; align-items: flex-start; gap: 14px; margin-bottom: 7px; }
  .contact__key {
    width: 16px; height: 16px; border-radius: 50%;
    background: #f1f1f1; font-size: 8px; font-weight: 700;
    display: flex; align-items: center; justify-content: center; flex: none; margin-top: 2px;
  }
  .contact__phone { font-size: 16px; font-weight: 700; letter-spacing: .5px; }
  .contact__text { font-size: 11px; line-height: 1.35; }
  .contact__web { font-size: 10px; letter-spacing: 3px; color: var(--ink-soft); }

  /* front panel */
  .front-frame { left: 485px; top: 51px; width: 242px; height: 361px; border: 2px solid var(--frame); }
  .front-bar { background: var(--coral); opacity: .85; }
  .front-bar--left { left: 461px; top: 80px; width: 13px; height: 377px; }
  .front-bar--right { left: 742px; top: 80px; width: 12px; height: 323px; }
  .thanks-box {
    left: 527px; top: 399px; width: 165px; height: 62px;
    background: var(--coral-deep);
    display: flex; align-items: center; justify-content: center;
    color: #fff; font-family: "Pacifico", cursive; font-size: 24px;
  }
  .thanks-langs {
    left: 414px; top: 474px; width: 400px; text-align: center;
    font-family: "Sorts Mill Goudy", Georgia, serif; font-size: 15px; line-height: 27px; color: var(--ink);
  }

  /* inside left */
  .story-box {
    left: 67px; top: 106px; width: 296px; height: 309px;
    background: var(--blush); border-radius: 26px;
    padding: 34px 24px 0 24px;
    font-style: italic; font-size: 13.5px; line-height: 1.38; color: var(--ink);
  }
  .story-box p + p { margin-top: 14px; }
  .argan-nuts {
    left: 98px; top: 343px; width: 210px; height: 154px;
    background: radial-gradient(ellipse 50% 45% at 50% 55%, #a8643a 0%, #7d4420 60%, rgba(125,68,32,0) 100%);
  }

  /* inside right */
  .benefits-title {
    left: 430px; top: 118px; width: 350px; text-align: center;
    font-size: 29px; font-weight: 800; color: var(--title-red); letter-spacing: .3px;
  }
  .benefits-title__lead { color: var(--title-red); }
  .benefits-title__rest { color: var(--coral); }
  .benefits-sub {
    left: 455px; top: 158px; width: 300px;
    display: flex; align-items: center; gap: 10px;
    font-size: 17px; font-weight: 600; color: var(--ink-soft); letter-spacing: 1px;
  }
  .benefits-sub::before, .benefits-sub::after { content: ""; flex: 1; height: 1px; background: #9a9a9a; }
  .benefits-list { left: 455px; top: 216px; list-style: none; }
  .benefits-list li {
    display: flex; align-items: center; gap: 10px;
    font-style: italic; font-size: 14.5px; height: 33px;
  }
  .benefits-list svg { flex: none; }
  .vegan-badge { left: 417px; top: 312px; width: 355px; height: 125px; }
  .site-link {
    left: 510px; top: 496px; width: 260px; text-align: center;
    font-size: 10px; letter-spacing: 3px; color: var(--ink-soft);
  }
</style>
</head>
<body>

<section class="spread spread--outside" aria-label="Outside of the card: back and front">
  <div class="feathers feathers--back" role="img" aria-label="Soft peach feathers photograph"></div>
  <div class="bottle bottle--dropper" role="img" aria-label="Photograph of a Kavro argan oil dropper bottle"></div>
  <div class="abs back-accent"></div>
  <div class="abs contact">
    <div class="contact__row"><span class="contact__key">P</span><span class="contact__phone">1234 123 1234</span></div>
    <div class="contact__row"><span class="contact__key">A</span><span class="contact__text">Lorem Ipsum is simply dummy text of the<br>printing and typesetting industry.</span></div>
    <div class="contact__row"><span class="contact__key">W</span><span class="contact__web">www.kavro-argan.com</span></div>
  </div>

  <div class="feathers feathers--front" role="img" aria-label="Soft peach feathers photograph"></div>
  <div class="abs front-bar front-bar--left"></div>
  <div class="abs front-bar front-bar--right"></div>
  <div class="abs front-frame"></div>
  <div class="bottle bottle--spray" role="img" aria-label="Photograph of a Kavro argan oil spray bottle"></div>
  <div class="abs thanks-box">Thank you</div>
  <p class="abs thanks-langs">Bedankt Merci Danke Shukran Grazie Tak Kop khun<br>Arigatô Hvala Dankie Mahalo</p>
</section>

<section class="spread spread--inside" aria-label="Inside of the card">
  <div class="feathers feathers--inside" role="img" aria-label="Soft peach feathers photograph"></div>

  <div class="abs story-box">
    <p>Wist u dat het Kavro team alles zelf doet, van de noot tot in het flesje. Met Kavro koopt u een 100% puur natuurproduct: volledig vrij van toevoegingen en bewaarmiddelen.</p>
    <p>U geeft uw huid, haar, nagels de allerbeste verzorging, op elk moment van de dag! Psoriasis, droge huid, eczeem, anti aging en zoveel meer voor heel het gezin.</p>
  </div>
  <div class="abs argan-nuts" role="img" aria-label="Photograph of argan nuts with leaves"></div>

  <h2 class="abs benefits-title"><span class="benefits-title__lead">PURE</span> <span class="benefits-title__rest">HEILZAAMHEID</span></h2>
  <p class="abs benefits-sub">IN ÉÉN TOPPRODUCT</p>
  <ul class="abs benefits-list">
    <li><svg width="20" height="20" viewBox="0 0 20 20"><circle cx="10" cy="10" r="9" fill="none" stroke="#e3303c" stroke-width="1.5"/><circle cx="10" cy="10" r="4" fill="#9a9a9a"/></svg>Een allesomvattende dag- en nachtverzorging</li>
    <li><svg width="20" height="20" viewBox="0 0 20 20"><circle cx="10" cy="10" r="9" fill="none" stroke="#e3303c" stroke-width="1.5"/><path d="M10 5c3 4 4 5.5 4 7a4 4 0 0 1-8 0c0-1.5 1-3 4-7z" fill="#9a9a9a"/></svg>Hydraterende en egaliserende eigenschappen</li>
    <li><svg width="20" height="20" viewBox="0 0 20 20"><circle cx="10" cy="10" r="9" fill="none" stroke="#e3303c" stroke-width="1.5"/><path d="M6 10.5l3 3 5-6" fill="none" stroke="#9a9a9a" stroke-width="2"/></svg>Herstellend bij huid-, haar- en nagel kwaaltjes</li>
  </ul>

  <svg class="abs vegan-badge" viewBox="0 0 355 125" aria-label="Vegan banner">
    <polygon points="62,28 345,8 340,88 50,110" fill="#ffffff" opacity=".9"/>
    <polygon points="78,22 330,4 324,84 68,104" fill="var(--vegan)"/>
    <polygon points="68,104 78,22 56,48 46,118" fill="var(--vegan-dark)"/>
    <text x="205" y="52" text-anchor="middle" font-family="Open Sans, sans-serif" font-weight="800" font-size="27" fill="#fff" transform="rotate(-4 205 52)">VEGAN</text>
    <text x="205" y="71" text-anchor="middle" font-family="Open Sans, sans-serif" font-style="italic" font-size="13" fill="#fff" transform="rotate(-4 205 71)">niet getest op dieren</text>
    <text x="205" y="87" text-anchor="middle" font-family="Open Sans, sans-serif" font-style="italic" font-size="13" fill="#fff" transform="rotate(-4 205 87)">100% ongeraffineerde Argan olie</text>
  </svg>

  <p class="abs site-link">www.kavro-argan.com</p>
</section>

</body>
</html>
```